Webdesign für Herstellung von Geschenk- und Dekorationsartikeln
Kobalt Prismo ist ein sehr angenehmer und professioneller Designer, der sich viele Gedanken über mein Projekt gemacht hat und ein Design, passend zu meinen Artikeln entworfen hat. Neben einer kompetenten Beratung gab es viele hilfreiche Vorschläge, die über den eigentlichen Auftrag hinaus gingen. Der Designer ist sehr zu empfehlen. Vielen Dank für den freundlichen Kontakt!
Zielgruppe
Wir sind eine kleine Firma, die mit einem Lasergravierer Geschenk- und Dekorationsartikel herstellt, verziert und beschriftet. Hierzu wird hauptsächlich Holz, Papier, Kork, Filz und Glas als Material eingesetzt.
Auch Schmuck , wie z.B. Kettenanhänger und Ohrringe aus Holz werden gefertigt.
Außerdem werden Fotogravur-Arbeiten nach Kundenwunsch angeboten.
Haupt-Zielgruppe sind Frauen ab 30.
Aufgabenstellung
Das Design soll etwas verspielt sein und Freude an den kleinen Dingen des Lebens ausdrücken. Es soll nicht zu sachlich und kühl sein.
Das vorhandene Logo wird bereit gestellt.
Es existiert noch keine Webseite. Die zukünftige Webseite soll über einen Shop verfügen.
Von der Shop-Darstellung her, hat mir die Webseite 'www.qvhauswerk.ch' gefallen.
Es wäre gut, wenn die im Logo vorhandenen Farben auch auf dem Design für die Webseite auftauchen würden.
Als Design-Tool wäre Adobe Photoshop (PSD) für die Erstellung gut.

```html
<!DOCTYPE html>
<html lang="de">
<head>
<meta charset="utf-8">
<title>Lunaveli – Holzcraft Ketten</title>
<link href="https://fonts.googleapis.com/css2?family=Hind:wght@500;600;700&display=swap" rel="stylesheet">
<style>
  :root {
    --cream: #f1e9e1;
    --white: #ffffff;
    --accent: #b5833f;
    --accent-button: #b98a49;
    --ring: #e7e0d8;
    --logo-grey: #6e6c69;
    --fabric-light: #cfa95a;
    --fabric-dark: #a98236;
    --wood-dark: #4a2c1e;
    --wood-mid: #6b4427;
  }
  html, body {
    margin: 0;
    padding: 0;
    width: 1200px;
    height: 2211px;
    overflow: hidden;
    background: var(--cream);
    font-family: "Hind", sans-serif;
  }
  .page {
    position: relative;
    width: 1200px;
    height: 2211px;
    overflow: hidden;
    background: var(--cream);
  }
  .bottom-wave {
    position: absolute;
    left: 0;
    top: 0;
    width: 1200px;
    height: 2211px;
  }
  .brand {
    position: absolute;
    left: 94px;
    top: 150px;
    font-size: 78px;
    font-weight: 500;
    color: var(--logo-grey);
    letter-spacing: 2px;
    line-height: 1;
  }
  .menu-button {
    position: absolute;
    left: 993px;
    top: 136px;
    width: 106px;
    height: 106px;
    border-radius: 50%;
    background: var(--accent);
  }
  .menu-button span {
    position: absolute;
    left: 30px;
    width: 46px;
    height: 5px;
    border-radius: 3px;
    background: var(--cream);
  }
  .menu-button span:nth-child(1) { top: 36px; }
  .menu-button span:nth-child(2) { top: 51px; }
  .menu-button span:nth-child(3) { top: 66px; }
  .hero-title {
    position: absolute;
    left: 88px;
    top: 434px;
    margin: 0;
    font-size: 122px;
    font-weight: 600;
    line-height: 143px;
    color: var(--accent);
  }
  .hero-tag {
    position: absolute;
    left: 94px;
    top: 728px;
    padding-left: 22px;
    border-left: 8px solid var(--accent);
    font-size: 36px;
    font-weight: 600;
    line-height: 39px;
    color: var(--accent);
  }
  .product-ring {
    position: absolute;
    left: 75px;
    top: 841px;
    width: 1036px;
    height: 1036px;
    border-radius: 50%;
    background: var(--ring);
  }
  .product-photo {
    position: absolute;
    left: 121px;
    top: 909px;
    width: 944px;
    height: 944px;
    border-radius: 50%;
    background:
      radial-gradient(ellipse 34% 34% at 50% 56%, var(--wood-dark) 0%, var(--wood-mid) 55%, rgba(107,68,39,0) 100%),
      radial-gradient(circle at 45% 40%, var(--fabric-light), var(--fabric-dark));
  }
  .cta {
    position: absolute;
    left: 399px;
    top: 1998px;
    width: 367px;
    height: 92px;
    border-radius: 46px;
    background: var(--accent-button);
    color: var(--white);
    font-size: 38px;
    font-weight: 600;
    line-height: 100px;
    text-align: center;
    text-decoration: none;
  }
</style>
</head>
<body>
<div class="page">
  <svg class="bottom-wave" viewBox="0 0 1200 2211" aria-hidden="true">
    <path d="M0 1726 C 250 1950, 600 2090, 1200 2104 L1200 2211 L0 2211 Z" fill="var(--white)"/>
  </svg>

  <div class="brand">Lunaveli</div>

  <div class="menu-button" aria-label="Menü"><span></span><span></span><span></span></div>

  <h1 class="hero-title">Holzcraft<br>Ketten</h1>
  <div class="hero-tag">Sommer Kollektion<br>Ketten</div>

  <div class="product-ring"></div>
  <div class="product-photo" role="img" aria-label="Produktfoto: Halskette mit dunklem, rautenförmigem Holzanhänger mit gelasertem Blütenmuster an schwarzer Kordel auf goldfarbenem Stoff"></div>

  <a class="cta" href="#">zum Produkt</a>
</div>
</body>
</html>
```